Guaranteed Job - Sleek Sexy Business Card UV Spot

Im looking for a sleek and sexy business card, that resembles elite or VIP status status.
our business is corinvale.example
you can view our products on there, but our main audience for handing out our cards will be for people in the hospitality industry, so it will need to impress high management and CEO of hotels and restaurants, bars, clubs etc...
the card features will have UV spot on both sides, 400gsm stock. standard size.
Artwork should be 86 x 54mm + 2mm bleed = 90 x 58mm
it should have a nice "unique" uv spot pattern that highlights the card, not a repeated pattern, theres no originality there, and it will be disregarded.
The written material will be:
Corin Vale Hospitality College (logo)
Tobin Marsh
Director
Phone: 1300 615 737
Mobile: 0455 817 296
Email: info@corinvale.example
website: www.corinvale.example
I'm looking for originality here, i don't want just a simple stock card, want something that has a wow factor for people.
You will find the logo attached. you may invert the white to black words to suit the background as you please.
thank you and good luck
As a side note, ive received a lot of proposals, im too busy to give feedback to each and every one, so if i havent provided feedback for your design within 24 hours, then consider it not acceptable, and you could resubmit another design.
So far i have not seen any design that stood out for me, they all seem pretty generic. there nothing thats unique, i would figure for the amount that im offering, that people would put some more effort and creativity into the design.
so far over 200 designs submitted, and nothing i have seen looks very original, everything looks like a different variation of the same stuff, i said it very clearly i wanted something unique, the only thing that has come close to it so far is this one
Reason: Ive received alot of design concepts and i have reviewed everyone, but i havent had time to give feedback to every single one, only the ones that have interested me, if i havent responded, its because i havent found it good enough.
so far only a few design have been on par with what ive been looking for, an attractive eye popping design.
heres a few of them,
http://files.pixelbazaar.example/design_img/51736/62418/62418_2840915_51736_image.jpg
http://files.pixelbazaar.example/design_img/51736/68254/68254_2841377_51736_image.jpg
theyre, both unique and original, and eye catching, the only thing theyre missing is the sexyness.
if you still think you have some creativity left in your minds, then throw it on here.
Reason: Sorry guys for the delay, I was in a serious accident and out of commission for the past few months, I'm just slowly recovering now, please bare with me as i try to attend to this project, it may take me awhile as I have other projects that are on standby, I'm not 100% at the moment, so im extending the deadline for 2 weeks right now. Thanks for your patience.
Hospitality

```html
<!DOCTYPE html>
<html lang="en">
<head>
<meta charset="utf-8">
<title>Corin Vale Hospitality College – Business Card Concepts</title>
<link rel="stylesheet" href="https://fonts.googleapis.com/css2?family=Barlow+Condensed:wght@600&family=Questrial&family=Open+Sans:wght@400;700&display=swap">
<style>
  :root {
    --stage: #000000;
    --orange: #f6a83a;
    --white: #ffffff;
    --ink: #111111;
    --rule: #8a8a8a;
    --band: #c8c8c8;
    --deep: #0c0c0c;
  }
  * { margin: 0; padding: 0; box-sizing: border-box; }
  html, body {
    width: 1200px;
    height: 900px;
    overflow: hidden;
    background: var(--stage);
  }
  .canvas {
    position: relative;
    width: 1200px;
    height: 900px;
    background: var(--stage);
  }
  .card {
    position: absolute;
    border-radius: 18px;
    overflow: hidden;
  }
  .card svg { position: absolute; inset: 0; display: block; }

  .card--stripes { left: 145px; top: 30px; width: 275px; height: 462px; background: var(--orange); }
  .card--brand   { left: 476px; top: 30px; width: 264px; height: 462px; background: var(--white); }
  .card--contact { left: 797px; top: 27px; width: 266px; height: 467px; background: var(--white); }

  .mount {
    position: absolute;
    left: 466px; top: 520px;
    width: 274px; height: 362px;
    background: var(--white);
  }
  .card--dark { left: 38px; top: 15px; width: 198px; height: 332px; background: var(--deep); border-radius: 14px; }

  .wordmark {
    position: absolute;
    font-family: "Barlow Condensed", "Arial Narrow", sans-serif;
    font-weight: 600;
    text-transform: uppercase;
    line-height: 0.95;
    display: flex;
    align-items: center;
    gap: 8px;
  }
  .wordmark__mark { width: 14px; height: 14px; background: currentColor; flex: none; }
  .wordmark__name { display: block; font-size: 22px; letter-spacing: 0.5px; }
  .wordmark__sub { display: block; font-size: 9px; letter-spacing: 0.8px; margin-top: 3px; }

  .card--stripes .wordmark { left: 50px; top: 345px; color: var(--white); }
  .card--brand .wordmark { left: 0; right: 0; top: 200px; justify-content: center; color: var(--orange); }
  .card--brand .wordmark__name { font-size: 30px; }
  .card--brand .wordmark__sub { font-size: 11px; }
  .card--dark .wordmark { left: 0; right: 0; top: 148px; justify-content: center; color: var(--orange); }

  .person {
    position: absolute;
    left: 0; right: 0; top: 54px;
    text-align: center;
    font-family: "Questrial", "Century Gothic", sans-serif;
    color: var(--ink);
  }
  .person__name { font-size: 28px; font-weight: 400; line-height: 1; }
  .person__role { font-size: 17px; margin-top: 8px; }
  .divider { position: absolute; left: 33px; width: 203px; top: 130px; height: 1px; background: var(--rule); }
  .company {
    position: absolute; left: 37px; top: 146px;
    font-family: "Open Sans", Arial, sans-serif;
    font-weight: 700; font-size: 11.5px; color: var(--ink);
  }
  .contact {
    position: absolute; left: 38px; top: 313px;
    list-style: none;
    font-family: "Open Sans", Arial, sans-serif;
    font-size: 13px; color: var(--ink);
  }
  .contact li { height: 26px; display: flex; align-items: center; }
  .contact li:nth-child(3) { height: 22px; }
  .contact__key { font-weight: 700; width: 17px; }
</style>
</head>
<body>
<main class="canvas">

  <section class="card card--stripes" aria-label="Card front, orange with diagonal stripes">
    <svg width="275" height="462" viewBox="0 0 275 462" aria-hidden="true">
      <polygon points="0,8 275,140 275,178 0,60" fill="var(--white)"/>
      <polygon points="0,105 275,237 275,277 0,155" fill="var(--white)"/>
      <polygon points="0,205 275,335 275,375 0,255" fill="var(--white)"/>
    </svg>
    <div class="wordmark">
      <span class="wordmark__mark"></span>
      <span>
        <span class="wordmark__name">Corin Vale</span>
        <span class="wordmark__sub">Hospitality College</span>
      </span>
    </div>
  </section>

  <section class="card card--brand" aria-label="Card back, brand name on white">
    <div class="wordmark">
      <span>
        <span class="wordmark__name">Corin Vale</span>
        <span class="wordmark__sub">Hospitality College</span>
      </span>
    </div>
  </section>

  <section class="card card--contact" aria-label="Card back, contact details">
    <svg width="266" height="467" viewBox="0 0 266 467" aria-hidden="true">
      <polygon points="0,170 266,292 266,326 0,213" fill="var(--band)"/>
    </svg>
    <div class="person">
      <p class="person__name">Tobin Marsh</p>
      <p class="person__role">Director</p>
    </div>
    <div class="divider"></div>
    <p class="company">Corin Vale Hospitality College</p>
    <ul class="contact">
      <li><span class="contact__key">T</span>1300 615 737</li>
      <li><span class="contact__key">M</span>0455 817 296</li>
      <li><span class="contact__key">E</span>info@corinvale.example</li>
      <li>www.corinvale.example</li>
    </ul>
  </section>

  <div class="mount">
    <section class="card card--dark" aria-label="Card variant, brand name on black">
      <div class="wordmark">
        <span>
          <span class="wordmark__name">Corin Vale</span>
          <span class="wordmark__sub">Hospitality College</span>
        </span>
      </div>
    </section>
  </div>

</main>
</body>
</html>
```